Design Business Card CORAL TIDE MOWING

We have attached a copy of our Logo, we like a business card designed with logo and mobile phone number on one side that stands out maybe gloss and on the other side it can have the services we do small picture of our logo name number, I have attached an idea to this that I have seen online, this is a business owned by a woman so we like pinks black and navy
Our logo is attached in pdf
Target Market(s)
Home owners that need lawns mowed
Industry/Entity Type
Lawns and gardens
Contact Information for Business Card
Logo business Owner name Dorinda Pask mobile number 0417296054
Font styles to use
Look and feel
Each slider illustrates characteristics of the customer's brand and the style your logo design should communicate.

```html
<!DOCTYPE html>
<html lang="en">
<head>
<meta charset="utf-8">
<title>Coral Tide Mowing – Business Card</title>
<link rel="stylesheet" href="https://fonts.googleapis.com/css2?family=Montserrat:wght@600;700;800&family=Great+Vibes&display=swap">
<style>
  :root {
    --stage: #2b2b2b;
    --navy: #02057a;
    --pink: #e0399b;
    --green: #2fb34a;
    --ink: #111111;
    --paper: #ffffff;
    --white: #ffffff;
  }
  * { box-sizing: border-box; margin: 0; padding: 0; }
  html, body { width: 1200px; height: 875px; overflow: hidden; }
  body {
    background: var(--stage);
    font-family: "Montserrat", Arial, sans-serif;
    display: flex;
    align-items: center;
    justify-content: center;
    gap: 40px;
  }
  .card {
    width: 540px;
    height: 309px;
    border-radius: 18px;
    position: relative;
    overflow: hidden;
  }

  /* Front */
  .card--front {
    background: var(--navy);
    display: flex;
    flex-direction: column;
    align-items: center;
    justify-content: center;
    gap: 26px;
  }
  .brand {
    display: flex;
    align-items: center;
    gap: 14px;
  }
  .brand__dot {
    width: 26px; height: 26px;
    border-radius: 50%;
    background: var(--pink);
  }
  .brand__name {
    color: var(--pink);
    font-weight: 800;
    font-size: 34px;
    letter-spacing: 1px;
  }
  .front__phone {
    color: var(--white);
    font-weight: 600;
    font-size: 34px;
    letter-spacing: 4px;
  }

  /* Back */
  .card--back {
    background: var(--paper);
    padding: 26px 30px 22px;
    display: flex;
    flex-direction: column;
  }
  .back__header {
    display: flex;
    justify-content: space-between;
    align-items: flex-start;
  }
  .owner__name {
    font-family: "Great Vibes", cursive;
    color: var(--pink);
    font-size: 44px;
    line-height: 1;
  }
  .owner__phone {
    color: var(--green);
    font-weight: 700;
    font-size: 24px;
    letter-spacing: 1px;
    margin-top: 2px;
  }
  .card--back .brand__name { font-size: 20px; }
  .card--back .brand__dot { width: 16px; height: 16px; }
  .card--back .brand { gap: 8px; margin-top: 8px; }

  .voucher {
    margin-top: 18px;
    display: flex;
    flex-direction: column;
    gap: 14px;
  }
  .voucher__row { display: flex; gap: 14px; }
  .field {
    flex: 1;
    display: flex;
    align-items: flex-end;
    gap: 6px;
    font-weight: 700;
    font-size: 12px;
    color: var(--ink);
    letter-spacing: .3px;
    white-space: nowrap;
  }
  .field__line {
    flex: 1;
    border-bottom: 2px dotted var(--ink);
    height: 12px;
  }
  .field--short { flex: 0 0 140px; }

  .services {
    margin-top: auto;
    color: var(--pink);
    font-weight: 700;
    font-size: 13px;
    line-height: 1.45;
    letter-spacing: .3px;
  }
  .services__dot { color: var(--green); padding: 0 3px; }
</style>
</head>
<body>

  <section class="card card--front" aria-label="Business card front">
    <div class="brand">
      <span class="brand__dot"></span>
      <span class="brand__name">CORAL TIDE MOWING</span>
    </div>
    <p class="front__phone">0417296054</p>
  </section>

  <section class="card card--back" aria-label="Gift voucher back">
    <header class="back__header">
      <div class="owner">
        <p class="owner__name">Dorinda Pask</p>
        <p class="owner__phone">0417296054</p>
      </div>
      <div class="brand">
        <span class="brand__dot"></span>
        <span class="brand__name">CORAL TIDE MOWING</span>
      </div>
    </header>

    <div class="voucher">
      <div class="voucher__row">
        <div class="field">A GIFT TO :<span class="field__line"></span></div>
        <div class="field field--short">NO :<span class="field__line"></span></div>
      </div>
      <div class="voucher__row">
        <div class="field">DATE :<span class="field__line"></span></div>
        <div class="field">FROM :<span class="field__line"></span></div>
      </div>
      <div class="voucher__row">
        <div class="field">VALUED AT :<span class="field__line"></span></div>
      </div>
    </div>

    <p class="services">
      MOWING<span class="services__dot">•</span>PLANTING<span class="services__dot">•</span>MULCHING<span class="services__dot">•</span>CLEAN-UP<br>
      FERTILIZING<span class="services__dot">•</span>WEEDING<span class="services__dot">•</span>TRIMMING<span class="services__dot">•</span>SODDING &amp; MORE
    </p>
  </section>

</body>
</html>
```